Dealer Price List June 2013

Simple, PDF price list for our customers. Word doc will be provided. Needs to be formatted nice and a design added. Product pictures will be provided. Only 2-3 pics per page plus company logo. 1 page, double sided flyer. Must be PDF only.
Updates

Additionally product details can be found at www.plinthmarrow.comĀ 

Industry/Entity Type

It Company

```html
<!DOCTYPE html>
<html lang="en">
<head>
<meta charset="utf-8">
<title>Plinth Marrow – 2013 Reseller Pricing</title>
<link rel="stylesheet" href="https://fonts.googleapis.com/css2?family=Source+Sans+3:ital,wght@0,400;0,600;0,700;1,400;1,600&display=swap">
<style>
  :root {
    --gold: #f4c246;
    --gold-deep: #e9ad2c;
    --ink: #1e1e1e;
    --rule: #9a9a9a;
    --panel: #ffffff;
    --brand-ink: #2b2213;
  }
  * { margin: 0; padding: 0; box-sizing: border-box; }
  html, body { width: 848px; height: 1200px; overflow: hidden; }
  body {
    position: relative;
    background: radial-gradient(ellipse at 50% 35%, var(--gold) 0%, var(--gold-deep) 100%);
    font-family: "Source Sans 3", "Myriad Pro", sans-serif;
    color: var(--ink);
  }
  .product-photo { position: absolute; z-index: 2; border: 3px solid #fff; border-top: none; }
  .photo-display-case {
    left: 8px; top: 0; width: 170px; height: 154px;
    background: linear-gradient(135deg, #c9d6e4 0%, #aebfd1 55%, #b98a6a 100%);
  }
  .photo-sleeve-pack {
    left: 702px; top: 0; width: 128px; height: 185px;
    background: linear-gradient(160deg, #3a3a3a 0%, #0d0d0d 60%, #262626 100%);
  }
  .brand-name {
    position: absolute; left: 0; right: 0; top: 40px;
    text-align: center;
    font-weight: 700; font-size: 44px; letter-spacing: 3px;
    text-transform: uppercase;
    color: var(--brand-ink);
  }
  .price-panel {
    position: absolute; left: 28px; top: 138px; width: 792px; height: 1038px;
    background: var(--panel);
    border-radius: 18px;
    box-shadow: 0 2px 6px rgba(0,0,0,0.25);
  }
  .panel-heading { position: absolute; left: 0; right: 0; text-align: center; }
  .heading-title { top: 9px; font-weight: 700; font-size: 20px; line-height: 25px; }
  .heading-terms { top: 67px; font-style: italic; font-size: 16px; letter-spacing: 0.2px; }
  .column-heads {
    position: absolute; left: 36px; right: 36px; top: 106px;
    display: flex; justify-content: space-between;
    font-weight: 700; font-size: 15px; letter-spacing: 1.2px;
    padding-bottom: 12px;
    border-bottom: 1.5px solid var(--rule);
  }
  .column-heads .price-head { width: 110px; }
  .price-list {
    position: absolute; left: 36px; right: 20px; top: 156px;
    list-style: none;
  }
  .price-row {
    display: flex; justify-content: space-between;
    height: 29.67px; line-height: 29.67px;
    font-size: 15px;
  }
  .price-row .price { width: 128px; }
  .price-row .spec { margin-left: 24px; }
</style>
</head>
<body>
  <div class="product-photo photo-display-case" role="img" aria-label="Product photo: signed ball in a clear display case"></div>
  <div class="brand-name">Plinth Marrow</div>
  <div class="product-photo photo-sleeve-pack" role="img" aria-label="Product photo: packaged pack of soft card sleeves"></div>

  <main class="price-panel">
    <p class="panel-heading heading-title">2013 Reseller Pricing - $500 Minimum Order<br>Effective June 1, 2013 – Mix and Match all products</p>
    <p class="panel-heading heading-terms">FREIGHT INCLUDED TO COMMERCIAL ADDRESSES – $29 Residential Surcharge</p>

    <div class="column-heads"><span>DESCRIPTION</span><span class="price-head">PRICE</span></div>

    <ul class="price-list">
      <li class="price-row"><span>Top-Load 3x4 Clear Card Holder (Case/1,000)</span><span class="price">$37.50/case</span></li>
      <li class="price-row"><span>Top-Load 3x4 “Rookie” Gold or Color Edge<span class="spec">25/1,000/18 lbs.</span></span><span class="price">$45/case</span></li>
      <li class="price-row"><span>Top-Load 3x4 1.5mm – 60 Pt. (Case/1,000)</span><span class="price">$65/case</span></li>
      <li class="price-row"><span>Top-Load 3x4 2.5mm – 100 Pt. (Case/500)</span><span class="price">$48/case</span></li>
      <li class="price-row"><span>Top-Load 3x4 3.5mm – 140 Pt. (Case/500)</span><span class="price">$69/case</span></li>
      <li class="price-row"><span>Top-Load 3x4 5mm – 190 Pt. (Case/250)</span><span class="price">$45/case</span></li>
      <li class="price-row"><span>Top-Load 3x4 7mm – 240 Pt. (Case/250)</span><span class="price">$49/case</span></li>
      <li class="price-row"><span>Top-Load 4x6 Photo (Case/500)</span><span class="price">$69/case</span></li>
      <li class="price-row"><span>Top-Load 6x4 Side Load Photo (Case/500)</span><span class="price">$69/case</span></li>
      <li class="price-row"><span>Top-Load 5x7 Photo (Case/500)</span><span class="price">$95/case</span></li>
      <li class="price-row"><span>Top-Load 6x9 Photo (Case/250)</span><span class="price">$65/case</span></li>
      <li class="price-row"><span>Top-Load Ticket (3 3/8”x 7 ¼”) (Case/500)</span><span class="price">$89/case</span></li>
      <li class="price-row"><span>Top-Load Reg. Currency (Case/500)</span><span class="price">$65/case</span></li>
      <li class="price-row"><span>Top-Load Large Currency (Case/250)</span><span class="price">$38/case</span></li>
      <li class="price-row"><span>Top-Load 8x10 Photo (Case/250)</span><span class="price">$99/case</span></li>
      <li class="price-row"><span>Top-Load 8.5x11 Photo/Document<span class="spec">(Case/250)</span></span><span class="price">$109/case</span></li>
      <li class="price-row"><span>Top-Load Thick Magazine 7mm (Case/50)</span><span class="price">$49/case</span></li>
      <li class="price-row"><span>Top-Load Super Thick Mag 10mm<span class="spec">(Case/50)</span></span><span class="price">$59/case</span></li>
      <li class="price-row"><span>Top-Load 11x14 Photo<span class="spec">(Case/100)</span></span><span class="price">$79/case</span></li>
      <li class="price-row"><span>Top-Load 11x17 Photo<span class="spec">(Case/100)</span></span><span class="price">$95/case</span></li>
      <li class="price-row"><span>Top-Load 16x20 Photo<span class="spec">(Case/50)</span></span><span class="price">$79/case</span></li>
      <li class="price-row"><span>Top-Load Pennant (Case/50)</span><span class="price">$89/case</span></li>
      <li class="price-row"><span>Top-Load 24x36 Poster (Case/10)</span><span class="price">$49/case</span></li>
      <li class="price-row"><span>Top-Load 29x43 Poster/Sheet (Case/10)</span><span class="price">$65/case</span></li>
      <li class="price-row"><span>Soft Card Sleeves (Case/10,000/100 packs)</span><span class="price">$32/case</span></li>
      <li class="price-row"><span>Thick Card Soft Sleeves (Case/10,000)</span><span class="price">$45/case</span></li>
      <li class="price-row"><span>Team Set Bags – Resealable (Case/5,000/50 packs)</span><span class="price">$62/case</span></li>
      <li class="price-row"><span>Graded Bags – Resealable (Case/5,000/50 packs)</span><span class="price">$65/case</span></li>
      <li class="price-row"><span>Postcard Soft Sleeves (Case/5,000/50 packs)</span><span class="price">$49/case</span></li>
    </ul>
  </main>
</body>
</html>
```